Save the date for wedding

A save the date for our wedding. We're looking for a simple and sleek invite. I would prefer not alot of calligraphy. Minimalism is good. The basic info to include is as follows:
Names: Mona and Felix
Date: June 9th
Where: Ottawa, Ontario
In small print please include that there will be a reception in Edmonton AB September 1st for those who cannot make it to Ottawa.
Please see the attached file for a style idea. Doesn’t have to be exactly like that, but something like that.

```html
<!DOCTYPE html>
<html lang="en">
<head>
<meta charset="utf-8">
<title>Save The Date – Mona &amp; Felix</title>
<link rel="stylesheet" href="https://fonts.googleapis.com/css2?family=Great+Vibes&family=Parisienne&family=Dancing+Script:wght@400&display=swap">
<style>
  :root {
    --paper: #f6edf4;
    --paper-light: #fdf9fc;
    --plum-deep: #6a2764;
    --plum: #7d3c78;
    --plum-soft: #94588f;
    --mauve: #b07aad;
    --petal: #c79bc5;
    --petal-pale: #e4cde2;
    --leaf: #a9cf8a;
  }
  * { box-sizing: border-box; margin: 0; padding: 0; }
  html, body { width: 848px; height: 1200px; overflow: hidden; background: var(--paper); }

  .card {
    position: relative;
    width: 848px;
    height: 1200px;
    overflow: hidden;
    background: radial-gradient(ellipse 60% 55% at 50% 50%, var(--paper-light) 0%, var(--paper) 100%);
    color: var(--plum-deep);
    text-align: center;
  }

  .floral-border {
    position: absolute;
    inset: 0;
    background:
      radial-gradient(ellipse 180px 140px at 60px 40px, var(--petal) 0%, rgba(199,155,197,0.55) 55%, transparent 100%),
      radial-gradient(ellipse 200px 130px at 790px 40px, var(--petal) 0%, rgba(199,155,197,0.55) 55%, transparent 100%),
      radial-gradient(ellipse 110px 520px at 20px 600px, var(--mauve) 0%, rgba(199,155,197,0.5) 55%, transparent 100%),
      radial-gradient(ellipse 110px 520px at 830px 620px, var(--mauve) 0%, rgba(199,155,197,0.5) 55%, transparent 100%),
      radial-gradient(ellipse 220px 130px at 120px 1170px, var(--petal) 0%, rgba(199,155,197,0.55) 55%, transparent 100%),
      radial-gradient(ellipse 240px 130px at 440px 1190px, var(--petal-pale) 0%, rgba(228,205,226,0.5) 55%, transparent 100%),
      radial-gradient(ellipse 220px 140px at 760px 1160px, var(--petal) 0%, rgba(199,155,197,0.55) 55%, transparent 100%);
  }

  .heading {
    position: absolute;
    left: 0; right: 0;
    top: 126px;
    font-family: "Great Vibes", cursive;
    font-weight: 400;
    font-size: 60px;
    line-height: 1;
    color: var(--plum);
  }
  .subheading {
    position: absolute;
    left: 0; right: 0;
    top: 214px;
    font-family: "Great Vibes", cursive;
    font-size: 32px;
    line-height: 1;
    color: var(--plum);
  }

  .couple-figure {
    position: absolute;
    left: 324px; top: 288px;
    width: 200px; height: 186px;
    background: linear-gradient(180deg, #9a6395 0%, #8a5287 100%);
    border-radius: 40px 40px 6px 6px;
    opacity: 0.85;
  }
  .flourish {
    position: absolute;
    top: 446px;
    width: 70px; height: 16px;
    border-radius: 8px;
    background: linear-gradient(90deg, transparent, #c46bbf);
  }
  .flourish--left { left: 238px; }
  .flourish--right { left: 538px; transform: scaleX(-1); }

  .names {
    position: absolute;
    left: 0; right: 0;
    top: 520px;
    font-family: "Great Vibes", cursive;
    font-size: 96px;
    line-height: 1;
    color: var(--plum-deep);
  }

  .date {
    position: absolute;
    left: 0; right: 0;
    top: 666px;
    font-family: "Great Vibes", cursive;
    font-size: 84px;
    line-height: 1;
    color: var(--plum);
  }
  .date .date__in { font-size: 46px; margin-right: 10px; }

  .location {
    position: absolute;
    left: 0; right: 0;
    top: 818px;
    display: flex;
    justify-content: center;
    align-items: center;
    gap: 14px;
    font-family: "Parisienne", cursive;
    font-size: 56px;
    line-height: 1;
    color: var(--plum-soft);
  }
  .location__divider {
    width: 14px; height: 40px;
    border-radius: 7px;
    background: var(--mauve);
  }

  .rule {
    position: absolute;
    left: 144px; top: 908px;
    width: 528px; height: 2px;
    background: linear-gradient(90deg, transparent, var(--plum-soft) 15%, var(--plum-soft) 85%, transparent);
  }

  .note {
    position: absolute;
    left: 0; right: 0;
    top: 930px;
    font-family: "Dancing Script", cursive;
    font-size: 21px;
    line-height: 37px;
    color: var(--plum);
  }
</style>
</head>
<body>
  <main class="card">
    <div class="floral-border" role="img" aria-label="Watercolour border of lilac magnolia petals and green leaves framing the card"></div>

    <h1 class="heading">Save The Date</h1>
    <p class="subheading">for Our Wedding</p>

    <div class="couple-figure" role="img" aria-label="Silhouette of a man kneeling to propose to a woman in a gown"></div>
    <div class="flourish flourish--left" role="img" aria-label="Curled ornamental flourish"></div>
    <div class="flourish flourish--right" role="img" aria-label="Curled ornamental flourish"></div>

    <h2 class="names">Mona &amp; Felix</h2>

    <p class="date"><span class="date__in">in</span>June 9th</p>

    <p class="location">
      <span>Ottawa</span>
      <span class="location__divider" role="img" aria-label="Small scroll ornament"></span>
      <span>Ontario</span>
    </p>

    <div class="rule"></div>

    <p class="note">there will be a reception in Edmonton AB September 1st<br>for those who cannot make it to Ottawa.</p>
  </main>
</body>
</html>
```